Marta Business Card

My wife is going to start her own business with renting holiday appartments to tourists. She needs a design for a new business card... and a new web site.
Look at Stayvolt "Erholung auf dem Lindenwäldchen"

Target Market(s)

Give business card to prospects at any situation

Contact Information for Business Card

not sure what this means

Font styles to use
Script

Colors
fec41a
fee18a

Requirements
Must have
• My wife's handwriting is difficult to read:
Entspannen - Loslassen - Auftanken
Marta & das Lindenwäldchen
Urlaub an einem besonderen Ort
Marta Brecke
Grauer Pfad 7
18471 Alt Feldow
post@marta-brecke.de
www.lindenwaeldchen.net
Nice to have
• Beige background
Font like handwriting

```html
<!DOCTYPE html>
<html lang="de">
<head>
<meta charset="utf-8">
<title>Marta &amp; das Lindenwäldchen – Visitenkarte</title>
<link rel="stylesheet" href="https://fonts.googleapis.com/css2?family=Pinyon+Script&display=swap">
<style>
  :root {
    --page-bg: #d9d9d9;
    --card-yellow: #fec41a;
    --band-dark: #231f20;
    --ink: #231f20;
  }
  html, body {
    margin: 0;
    padding: 0;
    width: 1200px;
    height: 908px;
    overflow: hidden;
    background: var(--page-bg);
  }
  .business-card {
    position: absolute;
    left: 100px;
    top: 156px;
    width: 1000px;
    height: 595px;
    background: var(--card-yellow);
    font-family: "Pinyon Script", cursive;
    color: var(--ink);
  }
  .tagline-band {
    position: absolute;
    left: 0;
    top: 0;
    width: 100%;
    height: 157px;
    background: var(--band-dark);
    display: flex;
    align-items: center;
    justify-content: center;
  }
  .tagline {
    margin: 0;
    color: var(--card-yellow);
    font-size: 54px;
    font-weight: normal;
    white-space: nowrap;
    letter-spacing: 0.5px;
  }
  .brand {
    position: absolute;
    left: 0;
    top: 218px;
    width: 100%;
    text-align: center;
  }
  .brand-name {
    margin: 0;
    font-size: 66px;
    font-weight: normal;
    line-height: 1;
  }
  .brand-claim {
    margin: 0;
    font-size: 40px;
    line-height: 1.1;
  }
  .contact-address {
    position: absolute;
    right: 550px;
    top: 414px;
    text-align: right;
    font-style: normal;
    font-size: 30px;
    line-height: 40px;
  }
  .contact-name {
    font-size: 34px;
    font-weight: bold;
    display: block;
  }
  .contact-divider {
    position: absolute;
    left: 498px;
    top: 461px;
    width: 2px;
    height: 70px;
    background: var(--ink);
  }
  .contact-online {
    position: absolute;
    left: 530px;
    top: 450px;
    font-size: 30px;
    line-height: 40px;
  }
</style>
</head>
<body>
  <section class="business-card">
    <div class="tagline-band">
      <p class="tagline">Entspannen - Loslassen - Auftanken</p>
    </div>
    <div class="brand">
      <h1 class="brand-name">Marta &amp; das Lindenwäldchen</h1>
      <p class="brand-claim">Urlaub an einem besonderen Ort</p>
    </div>
    <address class="contact-address">
      <span class="contact-name">Marta Brecke</span>
      Grauer Pfad 7<br>
      18471 Alt Feldow
    </address>
    <div class="contact-divider"></div>
    <div class="contact-online">
      post@marta-brecke.de<br>
      www.lindenwaeldchen.net
    </div>
  </section>
</body>
</html>
```